The World Most Wanted Eyelahes

1. We need a web design for a new company based in California, USA
2. We are the manufacturer for 100% human hair eyelashes,
made in Indonesia.
3. We recently launched "Tapered Eyelashes" with human hair.
Currently, none of the people carried Tapered eyelash.
4. We would like to see designs that use the 4 different colors that match with my products as "Four Seasons" concepts.
5. We prefer to follow www.quelmo.com style, like professional website.
6. Focus on products as a manufacturer, therefore, all wholesaler and retailer copy and paste to their marketing tools.
7. Need bilingual English and Spanish.
8. Easy to link with social media.

Target Market(s)

United States and Central/South America.

Industry/Entity Type

Hair

Number of Pages Required

5+ page

Requirements
Must have
• 1. Details of Products with image.
• 2. Hottest/Newest Items "Tapered in 100% Human Hair"
• 3. Store Page
Nice to have
• 1. My competitors is Vintrel Eyelash. http://www.vintrellashes.com/
• Please follow the concepts of it.
• 2. www.Quelmo.com: They have great products detail on the website.
• i would like to focus on "Tapered" for new styles of the eyelash.
• 3. I want to visitors can write down the "Reviews" in every single product.
• Please check the www.PRUBCosmetics.com.
Should not have
• It's not salon/Shop for the beauty.
• No need an appointment.
• We are the manufacturer of the eyelash.

```html
<!DOCTYPE html>
<html lang="en">
<head>
<meta charset="utf-8">
<title>Lumessa Eyelashes</title>
<link href="https://fonts.googleapis.com/css2?family=Oswald:wght@300;400;500;600&family=Open+Sans:wght@400;600&family=Cormorant+Garamond:wght@500&display=swap" rel="stylesheet">
<style>
:root{
  --canvas:#ececec;
  --page:#ffffff;
  --ink:#1e1e1e;
  --gold:#a8782f;
  --line:#e3e3e3;
  --star:#f0a21a;
  --badge:#d3202a;
  --navy:#1b3a6b;
  --footer:#151515;
  --footer-bottom:#0c0c0c;
  --footer-text:#b5b5b5;
  --footer-head:#ffffff;
}
*{margin:0;padding:0;box-sizing:border-box}
html,body{width:995px;height:1200px;overflow:hidden}
body{background:var(--canvas);font-family:"Open Sans",sans-serif;color:var(--ink);position:relative}
.page{position:absolute;left:82px;top:22px;width:832px;height:1178px;background:var(--page);box-shadow:0 0 6px rgba(0,0,0,.12)}
.brand{position:absolute;left:20px;top:34px;font-family:"Cormorant Garamond",serif;font-weight:500;font-size:50px;letter-spacing:1px;color:var(--gold);line-height:1;white-space:nowrap}
.brand small{display:block;font-family:"Open Sans",sans-serif;font-size:13px;letter-spacing:5px;color:#3a3a3a;margin-top:2px}
.social-top{position:absolute;left:455px;top:35px;display:flex;gap:4px}
.social-top span{width:24px;height:24px;border-radius:50%;background:#5a5a5a;display:block}
.search{position:absolute;left:605px;top:32px;width:158px;height:28px;border:1px solid var(--line);background:#fafafa;font-size:10px;color:#666;padding:7px 11px}
.search svg{position:absolute;right:10px;top:7px}
.cart{position:absolute;left:774px;top:26px;width:37px;height:37px;border:1.5px solid var(--navy);border-radius:50%}
.cart svg{position:absolute;left:11px;top:11px}
.cart b{position:absolute;right:-4px;top:-6px;width:16px;height:16px;border-radius:50%;background:var(--badge);color:#fff;font-size:8px;font-weight:400;text-align:center;line-height:16px}
.nav-rule{position:absolute;left:200px;right:0;top:86px;border-top:1px solid #f0f0f0}
.nav{position:absolute;top:98px;right:88px;display:flex;font-family:"Oswald",sans-serif;font-size:12px;font-weight:400;color:#333}
.nav span{padding:0 19px;line-height:28px;border-left:1px solid #eee;white-space:nowrap}
.nav span:first-child{border-left:0}
.lang{position:absolute;left:761px;top:101px;width:50px;height:23px;border:1px solid var(--line)}
.hero{position:absolute;left:0;top:139px;width:832px;height:413px;overflow:hidden;
  background:radial-gradient(ellipse at 72% 58%,#a8743a 0%,#6b421f 40%,#3a2212 75%,#24150b 100%)}
.hero-photo{position:absolute;left:0;top:0;width:470px;height:413px;
  background:radial-gradient(ellipse 55% 60% at 38% 45%,#c8936a 0%,#9c6a45 40%,rgba(110,70,40,.6) 70%,rgba(60,36,18,0) 100%),
             linear-gradient(180deg,#4a3020 0%,#7a5234 40%,#5a3a22 100%);
  -webkit-mask-image:linear-gradient(90deg,#000 70%,transparent 100%);mask-image:linear-gradient(90deg,#000 70%,transparent 100%)}
.hero h1{position:absolute;left:431px;top:178px;color:#fff;font-family:"Oswald",sans-serif;font-weight:500;font-size:46px;line-height:1;letter-spacing:-1px;white-space:nowrap}
.hero h2{position:absolute;left:431px;top:234px;color:#fff;font-family:"Oswald",sans-serif;font-weight:600;font-size:52px;line-height:1;letter-spacing:-2.5px;white-space:nowrap}
.arrow{position:absolute;top:221px;width:28px;height:28px;border-radius:50%;background:rgba(30,20,12,.75)}
.arrow svg{position:absolute;left:9px;top:8px}
.section-title{position:absolute;top:578px;left:0;right:0;text-align:center;font-family:"Oswald",sans-serif;font-weight:300;font-size:28px;color:var(--ink)}
.product{position:absolute;top:637px;width:174px}
.product .shot{height:178px;border:1px solid var(--line);padding:14px 22px 16px;background:#fbfbfb}
.product .shot div{width:100%;height:100%;border-radius:16px;box-shadow:inset 0 0 0 3px rgba(255,255,255,.5),0 2px 4px rgba(0,0,0,.15)}
.product h3{margin-top:12px;font-family:"Oswald",sans-serif;font-weight:400;font-size:11.5px;color:var(--ink);letter-spacing:-.2px;white-space:nowrap}
.product p{margin-top:7px;font-size:10px;color:#333;display:flex;align-items:center;gap:10px}
.stars{color:var(--star);font-size:9px}
.stars em{font-style:normal;color:#bbb}
.footer{position:absolute;left:0;top:900px;width:832px;height:222px;background:var(--footer)}
.footer .brand{left:20px;top:28px;font-size:50px}
.footer .about{position:absolute;left:22px;top:112px;width:220px;font-size:9.5px;line-height:17px;color:var(--footer-text)}
.col{position:absolute;top:30px}
.col h4{font-family:"Oswald",sans-serif;font-weight:400;font-size:13px;color:var(--footer-head);margin-bottom:14px}
.col li{list-style:none;font-size:10.5px;color:var(--footer-text);line-height:21.4px;white-space:nowrap}
.contact{font-size:10.5px;color:var(--footer-text);position:relative;padding-left:22px;white-space:nowrap}
.contact svg{position:absolute;left:0;top:2px}
.social-foot{position:absolute;left:648px;top:174px;display:flex;gap:8px}
.social-foot span{width:31px;height:31px;border-radius:50%;border:1.5px solid #777;display:block}
.social-foot span:first-child{border-color:#fff}
.bottom{position:absolute;left:0;top:1122px;width:832px;height:56px;background:var(--footer-bottom);text-align:center;font-size:10px;color:#8a8a8a;line-height:46px}
</style>
</head>
<body>
<div class="page">
  <header>
    <div class="brand">LUMESSA<small>EYELASHES</small></div>
    <div class="social-top" aria-label="Social media links">
      <span></span><span></span><span></span><span></span><span></span>
    </div>
    <div class="search">Search
      <svg width="13" height="13" viewBox="0 0 13 13"><circle cx="5.5" cy="5.5" r="4.2" fill="none" stroke="#444" stroke-width="1.8"/><line x1="8.6" y1="8.6" x2="12" y2="12" stroke="#444" stroke-width="2"/></svg>
    </div>
    <div class="cart">
      <svg width="14" height="13" viewBox="0 0 14 13"><path d="M0 1h2.5l2 7h7l2-5H3.5" fill="none" stroke="#1b3a6b" stroke-width="1.6"/><path d="M4 3h9l-1.8 4.5H5.2z" fill="#1b3a6b"/><circle cx="5.5" cy="11" r="1.2" fill="#1b3a6b"/><circle cx="10.5" cy="11" r="1.2" fill="#1b3a6b"/></svg>
      <b>0</b>
    </div>
    <div class="nav-rule"></div>
    <nav class="nav">
      <span>HOME</span><span>SHOP</span><span>PRODUCTS</span><span>BLOG</span><span>CONTACT US</span>
    </nav>
    <div class="lang" aria-label="Language selector">
      <svg width="50" height="23" viewBox="0 0 50 23"><rect x="8" y="6" width="21" height="12" fill="#1f3d8a"/><path d="M8 6l21 12M29 6L8 18" stroke="#fff" stroke-width="2.4"/><path d="M8 6l21 12M29 6L8 18" stroke="#c8102e" stroke-width="1"/><path d="M18.5 6v12M8 12h21" stroke="#fff" stroke-width="3.6"/><path d="M18.5 6v12M8 12h21" stroke="#c8102e" stroke-width="2"/><path d="M38 10l3 3 3-3" fill="none" stroke="#555" stroke-width="1.2"/></svg>
    </div>
  </header>

  <section class="hero">
    <div class="hero-photo" role="img" aria-label="Beauty portrait of a model with golden makeup and long lashes on a sparkling bronze background"></div>
    <h1>Tapered in</h1>
    <h2>100% HUMAN HAIR</h2>
    <div class="arrow" style="left:44px"><svg width="9" height="12" viewBox="0 0 9 12"><path d="M7 1L2 6l5 5" fill="none" stroke="#fff" stroke-width="2"/></svg></div>
    <div class="arrow" style="left:772px"><svg width="9" height="12" viewBox="0 0 9 12"><path d="M2 1l5 5-5 5" fill="none" stroke="#fff" stroke-width="2"/></svg></div>
  </section>

  <h2 class="section-title">FOUR SEASONS</h2>

  <article class="product" style="left:19px">
    <div class="shot"><div role="img" aria-label="Blue pack of individual lash clusters" style="background:radial-gradient(ellipse at 50% 30%,#f4d9dd 0%,rgba(244,217,221,0) 45%),linear-gradient(180deg,#dbe4ec 0%,#b9c8d6 45%,#1f2328 62%,#c9d6e2 80%,#eef2f5 100%)"></div></div>
    <h3>SED UT PERSPICIATIS UNDE OMNIS</h3>
    <p>2 Reviews <span class="stars">★★★<em>☆☆</em></span></p>
  </article>
  <article class="product" style="left:225px">
    <div class="shot"><div role="img" aria-label="Pink pack of strip lashes" style="background:linear-gradient(180deg,#f3d3dc 0%,#e8b8c8 50%,#f6f6f6 62%,#2a2a2a 72%,#f6e6ea 85%,#3a2e30 100%)"></div></div>
    <h3>SED UT PERSPICIATIS UNDE OMNIS</h3>
    <p>2 Reviews <span class="stars">★★★<em>☆☆</em></span></p>
  </article>
  <article class="product" style="left:431px">
    <div class="shot"><div role="img" aria-label="Blue pack of individual lash clusters" style="background:radial-gradient(ellipse at 50% 30%,#f4d9dd 0%,rgba(244,217,221,0) 45%),linear-gradient(180deg,#dbe4ec 0%,#b9c8d6 45%,#1f2328 62%,#c9d6e2 80%,#eef2f5 100%)"></div></div>
    <h3>SED UT PERSPICIATIS UNDE OMNIS</h3>
    <p>2 Reviews <span class="stars">★★★<em>☆☆</em></span></p>
  </article>
  <article class="product" style="left:637px">
    <div class="shot"><div role="img" aria-label="Gold pack of strip lashes" style="background:linear-gradient(180deg,#2b1a10 0%,#c98a3e 30%,#8a5526 55%,#dcdcdc 65%,#2a2a2a 74%,#7a4a22 85%,#2b1a10 100%)"></div></div>
    <h3>SED UT PERSPICIATIS UNDE OMNIS</h3>
    <p>2 Reviews <span class="stars">★★★<em>☆☆</em></span></p>
  </article>

  <footer class="footer">
    <div class="brand">LUMESSA</div>
    <p class="about">Lorem ipsum dolor sit amet conse ctetur adipisic-ing elit, sed do eiusmod tempor incididunt ut labore et dolore magna aliqua. Ut enim ad minim veniam, quis nostrud exercitation ullamco laboris nisi ut aliquip ex ea commodo</p>
    <div class="col" style="left:289px">
      <h4>OUR COMMUNITY</h4>
      <ul><li>Blog</li><li>Snapgram</li><li>Snapmeet sponsorships</li><li>Facepage</li><li>Chirper</li><li>Circles +</li><li>Newsletter Sign Up</li></ul>
    </div>
    <div class="col" style="left:480px">
      <h4>CUSTOMER SUPPORT</h4>
      <ul><li>Which GripStand</li><li>Should I Buy?</li><li>Support</li><li>Contact Us</li><li>Privacy Policy</li></ul>
    </div>
    <div class="col" style="left:644px">
      <h4>CONTACTS</h4>
      <p class="contact" style="line-height:17px"><svg width="11" height="13" viewBox="0 0 11 13"><path d="M5.5 12.5S1 7.5 1 5a4.5 4.5 0 019 0c0 2.5-4.5 7.5-4.5 7.5z" fill="#999"/><circle cx="5.5" cy="5" r="1.7" fill="#151515"/></svg>4578 lumessa.net Glasgow<br>DO4 GR P. O BOX 25994,</p>
      <p class="contact" style="margin-top:12px;font-size:12px;padding-left:19px"><svg width="12" height="12" viewBox="0 0 12 12"><path d="M2.5 1l2 2.5-1.2 1.5a7 7 0 003.7 3.7l1.5-1.2 2.5 2-1.3 1.5C5.5 11 1 6.5 1 2.3z" fill="#999"/></svg>Call Us: (900) 555-0142</p>
      <p class="contact" style="margin-top:10px;font-size:12px"><svg width="11" height="9" viewBox="0 0 11 9" style="top:4px"><rect width="11" height="9" fill="#999"/><path d="M0 0l5.5 4.5L11 0" fill="none" stroke="#151515" stroke-width="1"/></svg>info@lumessa.net</p>
    </div>
    <div class="social-foot" aria-label="Social media links"><span></span><span></span><span></span><span></span></div>
  </footer>
  <div class="bottom">All Rights Reserved. Copyrights @ 2015</div>
</div>
</body>
</html>
```